Postcard Design

Baxley is a vip taxi and hire car service that specializes in airport to hotel transfers and surrounding suburbs at affordable rates . we offer a personalize service with over 40 years industry experience. we would like to promote a special from melbourne cbd to airport for $65 , our contact number is 0481926370, email primecabride@brisolmail.com , facebook orbit cab and rental car services we plan on distributing these flyers at all major hotels

Industry/Entity Type

Hotel

```html
<!DOCTYPE html>
<html lang="en">
<head>
<meta charset="utf-8">
<title>Baxley Postcard</title>
<link rel="stylesheet" href="https://fonts.googleapis.com/css2?family=Anton&family=Oswald:wght@500;600&family=Lato:wght@400;700&display=swap">
<style>
  :root {
    --backdrop: #7a4b25;
    --yellow: #f6c12e;
    --yellow-deep: #e9ae1c;
    --black: #1c1c1c;
    --ink: #111111;
    --white: #ffffff;
    --light: #ececec;
    --rule: #9a9a9a;
    --stamp: #b3b3b3;
  }
  * { margin: 0; padding: 0; box-sizing: border-box; }
  html, body { width: 907px; height: 1200px; overflow: hidden; }
  body { background: var(--backdrop); position: relative; font-family: "Lato", sans-serif; }

  .card { position: absolute; left: 109px; width: 691px; overflow: hidden; }
  .card-front { top: 51px; height: 537px; background: linear-gradient(180deg, #dcdcdc 0%, var(--white) 45%, var(--light) 100%); }
  .card-back { top: 632px; height: 536px; background: var(--white); }

  .shapes { position: absolute; inset: 0; }

  .headline {
    position: absolute; right: 30px; top: 46px;
    font-family: "Anton", sans-serif; font-size: 82px; line-height: 1; color: var(--ink);
    letter-spacing: 1px;
  }
  .subhead {
    position: absolute; right: 27px; top: 130px;
    font-family: "Oswald", sans-serif; font-weight: 600; font-size: 29px; line-height: 1; color: var(--ink);
    letter-spacing: 0.5px;
  }
  .experience {
    position: absolute; right: 26px; top: 164px;
    font-size: 18px; font-weight: 700; color: var(--ink);
  }
  .offer { position: absolute; left: 352px; top: 232px; font-family: "Oswald", sans-serif; font-weight: 600; line-height: 1; }
  .offer-lead { font-size: 25px; color: var(--yellow); letter-spacing: 0.3px; }
  .offer-line { font-size: 29px; color: var(--white); margin-top: 9px; }
  .offer-price { font-size: 33px; color: var(--white); margin-top: 9px; }

  .call {
    position: absolute; left: 43px; top: 477px;
    font-family: "Oswald", sans-serif; font-weight: 600; font-size: 33px; line-height: 1; color: var(--white);
  }
  .call-number { color: var(--yellow); }

  .photo { position: absolute; }
  .photo-hands { left: 35px; top: 155px; width: 286px; height: 286px; border-radius: 50%;
    background: radial-gradient(circle at 60% 55%, #c89a7c 0%, #9aa3ab 45%, #6f7a82 100%); }
  .photo-sedan { left: 413px; top: 385px; width: 255px; height: 128px; border-radius: 40px 50px 12px 12px;
    background: linear-gradient(180deg, #6b6d70 0%, #3d3f42 60%, #2a2b2d 100%); }
  .photo-chauffeur { left: 0; top: 0; width: 321px; height: 166px;
    background: linear-gradient(180deg, #cfd6dc 0%, #b9c1c7 45%, #3a3b3d 75%, #6b6b6b 100%); }

  .story {
    position: absolute; left: 24px; top: 196px; width: 274px;
    font-size: 12.5px; line-height: 16.6px; color: var(--ink); text-align: justify; hyphens: auto;
  }
  .contact {
    position: absolute; left: 24px; top: 395px;
    font-size: 13px; color: var(--white);
  }
  .contact-phone { color: var(--yellow); font-size: 15px; margin-left: 2px; }

  .stamp { position: absolute; left: 609px; top: 26px; width: 45px; height: 47px; background: var(--stamp); }
  .address-line { position: absolute; left: 444px; width: 138px; height: 2px; background: var(--rule); }
</style>
</head>
<body>

<section class="card card-front">
  <svg class="shapes" width="691" height="537" viewBox="0 0 691 537" aria-hidden="true">
    <polygon points="0,0 268,0 322,457 0,457" fill="var(--yellow)"/>
    <polygon points="268,0 276,0 330,457 322,457" fill="var(--black)"/>
    <rect x="321" y="212" width="370" height="159" fill="var(--black)"/>
    <polygon points="395,479 691,479 691,537 412,537" fill="var(--yellow)"/>
    <polygon points="0,457 395,457 406,537 0,537" fill="var(--black)"/>
    <circle cx="178" cy="298" r="157" fill="var(--black)"/>
    <circle cx="178" cy="298" r="150" fill="var(--white)"/>
  </svg>
  <div class="photo photo-hands" role="img" aria-label="Hands holding a phone to book a ride on a city street"></div>

  <h1 class="headline">WE OFFER</h1>
  <p class="subhead">A PERSONALIZE SERVICE</p>
  <p class="experience">with over 40 years industry experience</p>

  <div class="offer">
    <p class="offer-lead">WE ARE PROMOTE A SPECIAL</p>
    <p class="offer-line">FROM MELBOURNE CBD</p>
    <p class="offer-price">TO AIRPORT FOR $65</p>
  </div>

  <div class="photo photo-sedan" role="img" aria-label="Dark grey sedan hire car"></div>

  <p class="call">CALL NOW <span class="call-number">0481926370</span></p>
</section>

<section class="card card-back">
  <svg class="shapes" width="691" height="536" viewBox="0 0 691 536" aria-hidden="true">
    <polygon points="0,166 321,166 331,366 0,366" fill="var(--yellow)"/>
    <polygon points="0,378 331,378 348,392 348,440 0,440" fill="var(--black)"/>
    <polygon points="331,366 348,378 331,378" fill="var(--black)"/>
  </svg>
  <div class="photo photo-chauffeur" role="img" aria-label="Chauffeur holding an umbrella beside a black sedan with a passenger seated inside"></div>

  <p class="story">Lorem Ipsum is simply dummy text of the printing and typesetting industry. Lorem Ipsum has been the industry's standard dummy text ever since the 1500s, when an unknown printer took a galley of type and scrambled it to make a type specimen book. It has survived not only five centuries, but also the leap into electronic typesetting, remaining essentially unchanged. Lorem Ipsum</p>

  <p class="contact">primecabride@brisolmail.com <span class="contact-phone">0481926370</span></p>

  <div class="stamp" aria-hidden="true"></div>
  <div class="address-line" style="top:218px"></div>
  <div class="address-line" style="top:244px"></div>
  <div class="address-line" style="top:266px"></div>
</section>

</body>
</html>
```